Small Business Consulting Firm Needs Business Card Design

Need a sleek modern business card with 2 sides matching the colors of our logo. We will be placing these with a mailer we are sending out. These business cards will only ever be given to business owners. We operate helping businesses who are struggling with cash flow or finances. If the green and blue design needs to be moved to the right of "Harborline Crest Consulting" for aesthetic purposes that is ok. We will need an editable file if possible. We would like to include the reps name, email, website, and phone number. For now just use Peter Vance, pvance@harborlinecrest.com, www.harborlinecrest.com, and 833-555-0172.

```html
<!DOCTYPE html>
<html lang="en">
<head>
<meta charset="utf-8">
<title>Harborline Crest Consulting – Business Card</title>
<link rel="stylesheet" href="https://fonts.googleapis.com/css2?family=Montserrat:wght@400;500&display=swap">
<style>
  :root {
    --card-bg: #ffffff;
    --card-edge: #000000;
    --ink: #111111;
    --brand-grey: #4a4a4a;
    --brand-blue: #0a7fc9;
    --brand-green: #6aab3c;
  }
  * { box-sizing: border-box; margin: 0; padding: 0; }
  html, body {
    width: 1200px; height: 691px; overflow: hidden;
    background: var(--card-bg);
    font-family: "Montserrat", sans-serif;
  }
  .card {
    position: relative;
    width: 1200px; height: 691px;
    border: 2px solid var(--card-edge);
    border-radius: 60px;
    background: var(--card-bg);
  }
  .brand {
    position: absolute;
    left: 96px; width: 400px; top: 290px;
    text-align: center;
    color: var(--brand-grey);
  }
  .brand-square {
    display: block;
    width: 54px; height: 54px;
    margin: 0 auto 26px;
    background: var(--brand-green);
  }
  .brand-name {
    font-weight: 400;
    font-size: 31px;
    letter-spacing: 0.06em;
    line-height: 1;
    white-space: nowrap;
  }
  .brand-tagline {
    margin-top: 14px;
    font-weight: 400;
    font-size: 14px;
    letter-spacing: 0.62em;
    padding-left: 0.62em;
    line-height: 1;
  }
  .rep {
    position: absolute;
    left: 603px; top: 192px;
    height: 57px;
    padding-left: 14px;
    border-left: 6px solid var(--brand-blue);
    display: flex; align-items: center;
  }
  .rep-name {
    font-weight: 400;
    font-size: 47px;
    color: var(--ink);
    letter-spacing: 0.01em;
    line-height: 1;
    margin-top: 8px;
  }
  .contacts {
    position: absolute;
    left: 603px; top: 344px;
    list-style: none;
  }
  .contact {
    display: flex; align-items: center;
    height: 58px;
    font-size: 28px;
    font-weight: 400;
    color: var(--ink);
    letter-spacing: 0.01em;
  }
  .contact-icon {
    width: 28px; height: 28px;
    margin-right: 10px;
    flex: none;
  }
</style>
</head>
<body>
  <main class="card">
    <section class="brand">
      <span class="brand-square"></span>
      <p class="brand-name">HARBORLINE CREST</p>
      <p class="brand-tagline">CONSULTING</p>
    </section>

    <header class="rep">
      <h1 class="rep-name">Peter Vance</h1>
    </header>

    <ul class="contacts">
      <li class="contact">
        <svg class="contact-icon" viewBox="0 0 28 28" aria-hidden="true">
          <rect x="2" y="6" width="24" height="17" fill="var(--ink)"/>
          <polyline points="2,7 14,16 26,7" fill="none" stroke="#fff" stroke-width="2"/>
          <polyline points="2,22 11,14 M26,22 17,14" fill="none" stroke="#fff" stroke-width="1.5"/>
          <line x1="2" y1="22" x2="11" y2="14" stroke="#fff" stroke-width="1.5"/>
          <line x1="26" y1="22" x2="17" y2="14" stroke="#fff" stroke-width="1.5"/>
        </svg>
        <span>pvance@harborlinecrest.com</span>
      </li>
      <li class="contact">
        <svg class="contact-icon" viewBox="0 0 28 28" aria-hidden="true">
          <g fill="none" stroke="var(--ink)" stroke-width="2">
            <circle cx="13" cy="13" r="11.5"/>
            <ellipse cx="13" cy="13" rx="5" ry="11.5"/>
            <line x1="1.5" y1="13" x2="24.5" y2="13"/>
            <line x1="13" y1="1.5" x2="13" y2="24.5"/>
          </g>
          <path d="M15 14 L27 21 L22 22 L25 27 L23 28 L20 23 L16 26 Z" fill="var(--ink)" stroke="#fff" stroke-width="1"/>
        </svg>
        <span>www.harborlinecrest.com</span>
      </li>
      <li class="contact">
        <svg class="contact-icon" viewBox="0 0 28 28" aria-hidden="true">
          <circle cx="14" cy="14" r="14" fill="var(--ink)"/>
          <rect x="10" y="7" width="8" height="14" rx="1.5" fill="none" stroke="#fff" stroke-width="1.6"/>
          <circle cx="14" cy="18.5" r="0.9" fill="#fff"/>
        </svg>
        <span>833-555-0172</span>
      </li>
    </ul>
  </main>
</body>
</html>
```